Looking for amazing PowerPoint Design for sustainable, green last mile delivery company

What we need
- PowerPoint master (16:9)
- Min. 20-30 most used template slides
- Templates for tables, processes, gantt chart, etc.
- Would be good to make it look very modern, green/sustainable, human
- Feel free to extend the color range in addition to the 2 colors from our logo

Who we are
- https://www.brookvane-cargo.de/index1.php
- Brookvane Cargo is a pioneer in urban green logistics and provides zero-emissions last mile delivery services for its logistics and retail clients
- we take on urban parcel delivery for our clients with a 100% electric commercial vehicles fleet, fair and sustainable working conditions for our employees and a unique professional customer-focused mindset
- We see ourselves as a professional services company who strongly cares about the environment, clients and their customers, and its employees

Attachements
- Company logos - see attached
- Licensed pictures (feel free to use in the designs ) - see here: https://www.filemarsh.example/sh/82qptmzc61w304/XXPnRtfa9gg254hjKLDWQ7Mxo?dl=0

Requirements
Must have
• We are thinking about at least the following content templates:

- intro/outro (e.g., title, agenda, transition, team, goals, about us, executive summary, key take aways, thank you)
- charts and graphs (e.g., pie, doughnut, bar, line, waterfall, venn)
- image and video (e.g., image only, large image with a sentence)
- text (e.g., text only, text with graph, text with 3/4/5 categories, key numbers)
- process (e.g., steps, phases)
- funnels
- pyramid
- frameworks (with 2/3/4/5 categories)
- timeline (e.g., general/project timeline, gantt)
- services offer
- KPIs/scorecard
- vision, mission, values, culture
- evaluation results
- activities/ToDo page
- policy
- career path
- icons page

Hope this helps. Pls see this as wish list as some of them can also be built by the content from the other slides

```html
<!DOCTYPE html>
<html lang="en">
<head>
<meta charset="utf-8">
<title>Brookvane Cargo – Master Slide Presentation</title>
<link rel="stylesheet" href="https://fonts.googleapis.com/css2?family=Montserrat:wght@400;500;600;700;800&display=swap">
<style>
:root{
  --green:#3a9b35;
  --deep:#1f7a34;
  --lime:#8cc63f;
  --dark:#2c2c2c;
  --ink:#333;
  --mute:#8a8a8a;
  --line:#e3e6e1;
  --paper:#ffffff;
  --bg:#eef0ec;
}
*{box-sizing:border-box;margin:0;padding:0}
html,body{width:1200px;height:4415px;overflow:hidden}
body{background:var(--bg);font-family:"Montserrat",sans-serif;color:var(--ink);position:relative}
.hero{position:absolute;left:0;top:0;width:1200px;height:1180px;display:flex;align-items:center;justify-content:center}
.hero-slide{width:760px;height:428px;background:var(--paper);box-shadow:0 20px 50px rgba(0,0,0,.12);position:relative;display:flex;flex-direction:column;align-items:center;justify-content:center}
.hero-slide .dot{width:90px;height:90px;border-radius:50%;background:var(--green);margin-bottom:22px}
.hero-slide b{font-size:46px;font-weight:800;color:var(--green);letter-spacing:1px}
.hero-slide i{font-style:normal;font-size:13px;font-weight:400;color:var(--mute);letter-spacing:4px;margin-top:12px}
.hero-slide .url{position:absolute;right:22px;top:50%;transform:rotate(90deg);transform-origin:right center;font-size:9px;color:var(--mute)}
.deck{position:absolute;top:1219px;left:24px;display:grid;grid-template-columns:repeat(3,372px);grid-auto-rows:209px;column-gap:18px;row-gap:19px}
.slide{position:relative;background:var(--paper);overflow:hidden;box-shadow:0 2px 8px rgba(0,0,0,.08)}
.slide.dark{background:var(--dark);color:#fff}
.slide.greenbg{background:linear-gradient(135deg,var(--green),var(--deep))}
.foot{position:absolute;left:0;right:0;bottom:0;height:3px;background:linear-gradient(90deg,var(--deep),var(--lime))}
.t{position:absolute;top:12px;left:14px;font-size:11px;font-weight:700;color:var(--ink)}
.mark{position:absolute;top:10px;right:12px;display:flex;align-items:center;gap:3px;font-size:6px;font-weight:700;color:var(--green);text-transform:uppercase;white-space:nowrap}
.mark::before{content:"";width:9px;height:9px;border-radius:50%;background:var(--green)}
.p{font-size:4.6px;line-height:1.5;color:var(--mute)}
.h{font-size:5.5px;font-weight:700;color:var(--green);margin-bottom:2px}
.ph{background:linear-gradient(135deg,#9ccf6a,#4f8f3a)}
.ph.soft{background:linear-gradient(135deg,#e7efe2,#b7d39c)}
.ph.people{background:linear-gradient(160deg,#c9b7a4,#6b5a4e)}
.ph.road{background:linear-gradient(160deg,#6fae5a,#2f6b3a)}
.abs{position:absolute}
.brand-c{position:absolute;inset:0;display:flex;flex-direction:column;align-items:center;justify-content:center}
.brand-c .dot{width:38px;height:38px;border-radius:50%;background:var(--green);margin-bottom:8px}
.brand-c b{font-size:17px;font-weight:800;color:var(--green);white-space:nowrap}
.brand-c i{font-style:normal;font-size:5px;font-weight:400;color:var(--mute);letter-spacing:2px;margin-top:4px}
.dark .brand-c b{color:var(--lime)}
.dark .brand-c i{color:#aaa}
.master-t{font-size:12px;font-weight:700;line-height:1.2}
.sub{font-size:4.5px;letter-spacing:2px;color:var(--mute);margin-top:3px}
.num{width:16px;height:16px;border-radius:50%;background:var(--green);color:#fff;font-size:7px;font-weight:700;display:flex;align-items:center;justify-content:center;flex:none}
.num.dk{background:var(--dark)}
.row{display:flex;gap:5px;align-items:flex-start}
.cols{position:absolute;top:40px;left:14px;right:14px;display:grid;gap:12px}
</style>
</head>
<body>

<section class="hero">
  <div class="hero-slide">
    <span class="dot"></span>
    <b>BROOKVANE CARGO</b>
    <i>ZERO-EMISSION CITY DELIVERY</i>
    <span class="url">www.brookvane-cargo.de</span>
  </div>
</section>

<main class="deck">

  <div class="slide"><div class="brand-c"><span class="dot"></span><b>BROOKVANE CARGO</b><i>ZERO-EMISSION CITY DELIVERY</i></div></div>

  <div class="slide dark"><div class="brand-c"><span class="dot"></span><b>BROOKVANE CARGO</b><i>ZERO-EMISSION CITY DELIVERY</i></div></div>

  <div class="slide">
    <div class="abs" style="left:-30px;top:10px;width:200px;height:200px;border-radius:50%;background:linear-gradient(135deg,var(--lime),var(--green))"></div>
    <div class="mark" style="top:22px;right:auto;left:228px;font-size:7px">Brookvane Cargo</div>
    <div class="abs" style="left:228px;top:90px"><div class="master-t">Master Slide<br>Presentation</div><div class="sub">SUBTITLE HERE</div></div>
    <div class="abs p" style="right:10px;bottom:8px">March 2021</div>
  </div>

  <div class="slide">
    <div class="mark" style="top:28px;right:auto;left:14px;font-size:7px">Brookvane Cargo</div>
    <div class="abs" style="left:14px;top:100px"><div class="master-t">Master Slide<br>Presentation</div><div class="sub">SUBTITLE HERE</div></div>
    <div class="abs ph road" role="img" aria-label="Heart-shaped frame with delivery van photo" style="right:20px;top:14px;width:180px;height:180px;border-radius:50%"></div>
    <div class="foot"></div>
  </div>

  <div class="slide dark">
    <div class="mark" style="top:28px;right:auto;left:14px;font-size:7px;color:var(--lime)">Brookvane Cargo</div>
    <div class="abs" style="left:14px;top:100px"><div class="master-t" style="color:var(--lime)">Master Slide<br>Presentation</div><div class="sub">SUBTITLE HERE</div></div>
    <div class="abs ph road" role="img" aria-label="Heart-shaped frame with delivery van photo" style="right:20px;top:14px;width:180px;height:180px;border-radius:50%"></div>
  </div>

  <div class="slide ph road" role="img" aria-label="Green toned photo of an electric delivery van">
    <div class="mark" style="left:50%;right:auto;transform:translateX(-50%);color:#fff;top:14px">Brookvane Cargo</div>
    <div class="abs" style="left:0;right:0;top:88px;text-align:center;color:#fff"><div class="p" style="color:#e8f4dc;letter-spacing:2px">WWW.BROOKVANE-CARGO.DE</div><div style="font-size:14px;font-weight:700;margin-top:4px">Master Slide Presentation</div><div style="display:inline-block;margin-top:6px;background:var(--deep);font-size:4px;padding:2px 6px">PRESENTATION</div></div>
  </div>

  <div class="slide">
    <div class="abs" style="left:0;top:0;width:90px;height:209px;background:var(--dark)"><div class="mark" style="left:10px;right:auto;color:var(--lime);font-size:5px">Brookvane Cargo</div><div class="abs" style="left:10px;top:100px;font-size:11px;font-weight:700;color:var(--lime)">Agenda</div></div>
    <div class="abs ph soft" role="img" aria-label="Hands holding a young tree" style="left:90px;top:0;width:130px;height:209px"></div>
    <div class="abs" style="left:236px;top:30px;right:14px;font-size:6px;line-height:28px">
      <div style="border-bottom:1px solid var(--line)">Introduction</div><div style="border-bottom:1px solid var(--line)">About Us</div><div style="border-bottom:1px solid var(--line)">Welcome Message</div><div style="border-bottom:1px solid var(--line)">Our Services</div><div style="border-bottom:1px solid var(--line)">Our Team</div><div>Contact Us</div>
    </div>
  </div>

  <div class="slide"><div class="t">Table Of Content</div><div class="mark">Brookvane Cargo</div>
    <div class="cols" style="grid-template-columns:1fr 1fr;row-gap:12px">
      <div class="row"><span style="font-size:22px;color:#ccc;font-weight:300">1</span><div><div class="h">Content here</div><div class="p">Add a short note here to explain this point.</div></div></div>
      <div class="row"><span style="font-size:22px;color:#ccc;font-weight:300">4</span><div><div class="h">Content here</div><div class="p">Add a short note here to explain this point.</div></div></div>
      <div class="row"><span style="font-size:22px;color:#ccc;font-weight:300">2</span><div><div class="h">Content here</div><div class="p">Add a short note here to explain this point.</div></div></div>
      <div class="row"><span style="font-size:22px;color:#ccc;font-weight:300">5</span><div><div class="h">Content here</div><div class="p">Add a short note here to explain this point.</div></div></div>
      <div class="row"><span style="font-size:22px;color:#ccc;font-weight:300">3</span><div><div class="h">Content here</div><div class="p">Add a short note here to explain this point.</div></div></div>
      <div class="row"><span style="font-size:22px;color:#ccc;font-weight:300">6</span><div><div class="h">Content here</div><div class="p">Add a short note here to explain this point.</div></div></div>
    </div><div class="foot"></div></div>

  <div class="slide"><div class="t">Welcome Message</div><div class="mark">Brookvane Cargo</div>
    <div class="abs" style="left:40px;top:78px;width:40px;height:40px;border-radius:50%;border:2px solid var(--lime);display:flex;align-items:center;justify-content:center;font-size:26px;font-weight:800;color:var(--green);line-height:1">&rdquo;</div>
    <div class="abs p" style="left:180px;top:70px;right:20px">You can simply impress your audience and add a unique zing and appeal to your presentation. Easy to change colors, photos and text. Get a modern presentation that is beautifully designed and ready to use.<div style="text-align:right;margin-top:4px">— Team Lead</div></div>
    <div class="foot"></div></div>

  <div class="slide"><div class="t">Timeline</div><div class="mark">Brookvane Cargo</div>
    <svg class="abs" style="left:14px;top:40px" width="344" height="150" viewBox="0 0 344 150">
      <text x="0" y="58" font-size="8" fill="#333" font-family="Montserrat">Start</text>
      <line x1="20" y1="65" x2="300" y2="65" stroke="#bbb" stroke-width="1"/>
      <g fill="#3a9b35"><circle cx="70" cy="65" r="3"/><circle cx="120" cy="65" r="3"/><circle cx="170" cy="65" r="3"/><circle cx="220" cy="65" r="3"/></g>
      <circle cx="290" cy="65" r="9" fill="#8cc63f"/>
      <text x="278" y="50" font-size="7" fill="#8cc63f" font-family="Montserrat">Vision</text>
      <g font-size="4" fill="#999" font-family="Montserrat"><text x="62" y="80">2016</text><text x="112" y="80">2018</text><text x="162" y="80">2020</text><text x="212" y="80">2022</text></g>
      <g stroke="#ccc"><line x1="95" y1="65" x2="95" y2="30"/><line x1="145" y1="65" x2="145" y2="30"/><line x1="195" y1="65" x2="195" y2="30"/></g>
    </svg><div class="foot"></div></div>

  <div class="slide"><div class="t">Gantt Chart</div><div class="mark">Brookvane Cargo</div>
    <svg class="abs" style="left:14px;top:32px" width="344" height="165" viewBox="0 0 344 165">
      <rect x="0" y="0" width="344" height="8" fill="#3a9b35"/>
      <rect x="0" y="0" width="30" height="165" fill="#2c2c2c"/>
      <g stroke="#e3e6e1" stroke-width=".6">
        <line x1="30" y1="20" x2="344" y2="20"/><line x1="30" y1="35" x2="344" y2="35"/><line x1="30" y1="50" x2="344" y2="50"/><line x1="30" y1="65" x2="344" y2="65"/><line x1="30" y1="80" x2="344" y2="80"/><line x1="30" y1="95" x2="344" y2="95"/><line x1="30" y1="110" x2="344" y2="110"/><line x1="30" y1="125" x2="344" y2="125"/><line x1="30" y1="140" x2="344" y2="140"/><line x1="30" y1="155" x2="344" y2="155"/>
        <line x1="80" y1="8" x2="80" y2="165"/><line x1="130" y1="8" x2="130" y2="165"/><line x1="180" y1="8" x2="180" y2="165"/><line x1="230" y1="8" x2="230" y2="165"/><line x1="280" y1="8" x2="280" y2="165"/>
      </g>
      <rect x="40" y="24" width="90" height="7" fill="#8cc63f"/><rect x="110" y="39" width="80" height="7" fill="#2c2c2c"/><rect x="150" y="54" width="120" height="7" fill="#3a9b35"/><rect x="90" y="69" width="90" height="7" fill="#8cc63f"/><rect x="180" y="84" width="70" height="7" fill="#3a9b35"/><rect x="60" y="99" width="60" height="7" fill="#2c2c2c"/><rect x="250" y="114" width="60" height="7" fill="#8cc63f"/><rect x="130" y="144" width="110" height="7" fill="#2c2c2c"/>
    </svg><div class="foot"></div></div>

  <div class="slide"><div class="t">Your Title Here - One Column</div><div class="mark">Brookvane Cargo</div>
    <div class="abs" style="left:14px;top:52px;width:150px"><div class="h">Content Here</div><div class="p">You can simply impress your audience and add a unique zing and appeal to your presentation. Easy to change colors, photos and text. Get a modern presentation that is beautifully designed.</div></div>
    <div class="abs" style="right:30px;top:50px;width:120px;height:120px;border-radius:50%;background:#f1f6ec"></div><div class="foot"></div></div>

  <div class="slide"><div class="t">Your Title Here - Two Column</div><div class="mark">Brookvane Cargo</div>
    <div class="cols" style="grid-template-columns:1fr 1fr;top:50px"><div><div class="h">Content Here</div><div class="p">You can simply impress your audience and add a unique zing and appeal to your presentation. Easy to change colors, photos and text.</div></div><div><div class="h">Content Here</div><div class="p">You can simply impress your audience and add a unique zing and appeal to your presentation. Easy to change colors, photos and text.</div></div></div><div class="foot"></div></div>

  <div class="slide"><div class="t">Your Title Here - Three Column</div><div class="mark">Brookvane Cargo</div>
    <div class="cols" style="grid-template-columns:1fr 1fr 1fr;top:50px"><div><div class="h">Content Here</div><div class="p">You can simply impress your audience and add a unique zing and appeal to your presentation. Easy to change colors, photos and text.</div></div><div><div class="h">Content Here</div><div class="p">You can simply impress your audience and add a unique zing and appeal to your presentation. Easy to change colors, photos and text.</div></div><div><div class="h">Content Here</div><div class="p">You can simply impress your audience and add a unique zing and appeal to your presentation. Easy to change colors, photos and text.</div></div></div><div class="foot"></div></div>

  <div class="slide"><div class="t">Your Title Here</div><div class="mark">Brookvane Cargo</div>
    <div class="abs p" style="left:14px;top:55px;width:140px">You can simply impress your audience and add a unique zing and appeal to your presentation. Easy to change colors, photos and text.</div>
    <div class="abs h" style="left:190px;top:38px">Image With A Sentence</div>
    <div class="abs ph" role="img" aria-label="Single tree standing between dry and green land" style="left:170px;top:48px;width:180px;height:120px"></div><div class="foot"></div></div>

  <div class="slide"><div class="t">Bullets Points/Key Numbers</div><div class="mark">Brookvane Cargo</div>
    <div class="cols" style="grid-template-columns:1fr 1fr;row-gap:10px;top:44px">
      <div class="row"><span class="num">1</span><div><div class="h">Content Title here</div><div class="p">Add a short note here to explain this point.</div></div></div>
      <div class="row"><span class="num">4</span><div><div class="h">Content Title here</div><div class="p">Add a short note here to explain this point.</div></div></div>
      <div class="row"><span class="num" style="background:var(--lime)">2</span><div><div class="h">Content Title here</div><div class="p">Add a short note here to explain this point.</div></div></div>
      <div class="row"><span class="num" style="background:var(--lime)">5</span><div><div class="h">Content Title here</div><div class="p">Add a short note here to explain this point.</div></div></div>
      <div class="row"><span class="num dk">3</span><div><div class="h">Content Title here</div><div class="p">Add a short note here to explain this point.</div></div></div>
      <div class="row"><span class="num dk">6</span><div><div class="h">Content Title here</div><div class="p">Add a short note here to explain this point.</div></div></div>
    </div><div class="foot"></div></div>

  <div class="slide"><div class="t">Your Title Here</div><div class="mark">Brookvane Cargo</div>
    <div class="abs" style="left:14px;right:14px;top:36px">
      <div class="row" style="border-bottom:1px solid var(--line);padding:6px 0"><div class="h" style="width:70px">Content Here</div><div class="p">Add a short note here to explain this point in one line.</div></div>
      <div class="row" style="border-bottom:1px solid var(--line);padding:6px 0"><div class="h" style="width:70px">Content Here</div><div class="p">Add a short note here to explain this point in one line.</div></div>
      <div class="row" style="border-bottom:1px solid var(--line);padding:6px 0"><div class="h" style="width:70px">Content Here</div><div class="p">Add a short note here to explain this point in one line.</div></div>
      <div class="row" style="padding:6px 0"><div class="h" style="width:70px">Content Here</div><div class="p">Add a short note here to explain this point in one line.</div></div>
    </div><div class="foot"></div></div>

  <div class="slide"><div class="abs ph" role="img" aria-label="Two hands reaching toward each other over green foliage" style="left:0;top:0;right:0;height:150px"></div>
    <div class="abs" style="left:14px;top:12px;font-size:11px;font-weight:700;color:#fff">Big Picture with Text</div>
    <div class="abs p" style="left:30px;right:30px;top:160px;text-align:center">You can simply impress your audience and add a unique zing and appeal to your presentation with a large image.</div><div class="foot"></div></div>

  <div class="slide"><div class="t">Infographic Diagrams</div><div class="mark">Brookvane Cargo</div>
    <svg class="abs" style="left:20px;top:40px" width="130" height="160" viewBox="0 0 130 160">
      <path d="M70 10 A70 70 0 0 1 70 150" fill="none" stroke="#ddd" stroke-width="1"/>
      <circle cx="60" cy="80" r="22" fill="#f1f6ec"/><circle cx="60" cy="80" r="9" fill="#3a9b35"/>
      <circle cx="98" cy="25" r="9" fill="#3a9b35"/><circle cx="120" cy="62" r="9" fill="#8cc63f"/><circle cx="120" cy="100" r="9" fill="#999"/><circle cx="98" cy="138" r="9" fill="#2c2c2c"/>
    </svg>
    <div class="abs" style="left:170px;top:48px;width:180px;display:grid;row-gap:7px">
      <div><div class="h">Content Title</div><div class="p">Add a short note here to explain this point.</div></div><div><div class="h">Content Title</div><div class="p">Add a short note here to explain this point.</div></div><div><div class="h">Content Title</div><div class="p">Add a short note here to explain this point.</div></div><div><div class="h">Content Title</div><div class="p">Add a short note here to explain this point.</div></div>
    </div><div class="foot"></div></div>

  <div class="slide"><div class="t">Pie Charts</div><div class="mark">Brookvane Cargo</div>
    <div class="abs p" style="left:60px;right:60px;top:34px;text-align:center">Add a short note here to explain these charts. Easy to change colors and text.</div>
    <svg class="abs" style="left:30px;top:70px" width="312" height="70" viewBox="0 0 312 70">
      <g fill="none" stroke-width="6" transform="rotate(-90)">
        <circle cx="-35" cy="40" r="24" stroke="#e3e6e1"/><circle cx="-35" cy="40" r="24" stroke="#3a9b35" stroke-dasharray="102.5 150.8"/>
        <circle cx="-35" cy="156" r="24" stroke="#e3e6e1"/><circle cx="-35" cy="156" r="24" stroke="#8cc63f" stroke-dasharray="52.8 150.8"/>
        <circle cx="-35" cy="272" r="24" stroke="#e3e6e1"/><circle cx="-35" cy="272" r="24" stroke="#2c2c2c" stroke-dasharray="82.9 150.8"/>
      </g>
      <g font-family="Montserrat" font-weight="700" font-size="11" text-anchor="middle"><text x="40" y="39" fill="#3a9b35">68%</text><text x="156" y="39" fill="#8cc63f">35%</text><text x="272" y="39" fill="#2c2c2c">55%</text></g>
    </svg>
    <div class="abs p" style="left:40px;top:150px;width:60px;text-align:center">Add a short note here.</div><div class="abs p" style="left:156px;top:150px;width:60px;text-align:center">Add a short note here.</div><div class="abs p" style="left:272px;top:150px;width:60px;text-align:center">Add a short note here.</div>
    <div class="foot"></div></div>

  <div class="slide"><div class="t">Bar Chart</div><div class="mark">Brookvane Cargo</div>
    <svg class="abs" style="left:14px;top:40px" width="344" height="150" viewBox="0 0 344 150">
      <g stroke="#eee"><line x1="30" y1="20" x2="340" y2="20"/><line x1="30" y1="50" x2="340" y2="50"/><line x1="30" y1="80" x2="340" y2="80"/><line x1="30" y1="110" x2="340" y2="110"/></g>
      <g font-family="Montserrat" font-size="5" fill="#999"><text x="5" y="22">2000</text><text x="5" y="52">1500</text><text x="5" y="82">1000</text><text x="5" y="112">500</text></g>
      <g><rect x="50" y="60" width="10" height="60" fill="#8cc63f"/><rect x="80" y="40" width="10" height="80" fill="#e3e6e1"/><rect x="110" y="30" width="10" height="90" fill="#3a9b35"/><rect x="140" y="55" width="10" height="65" fill="#2c2c2c"/><rect x="170" y="35" width="10" height="85" fill="#8cc63f"/><rect x="200" y="45" width="10" height="75" fill="#e3e6e1"/><rect x="230" y="25" width="10" height="95" fill="#2c2c2c"/><rect x="260" y="50" width="10" height="70" fill="#3a9b35"/><rect x="290" y="30" width="10" height="90" fill="#2c2c2c"/><rect x="320" y="40" width="10" height="80" fill="#3a9b35"/></g>
      <g font-family="Montserrat" font-size="4.5" fill="#999"><text x="47" y="130">2011</text><text x="77" y="130">2012</text><text x="107" y="130">2013</text><text x="137" y="130">2014</text><text x="167" y="130">2015</text><text x="197" y="130">2016</text><text x="227" y="130">2017</text><text x="257" y="130">2018</text><text x="287" y="130">2019</text><text x="317" y="130">2020</text></g>
    </svg><div class="foot"></div></div>

  <div class="slide"><div class="t">Table Chart</div><div class="mark">Brookvane Cargo</div>
    <svg class="abs" style="left:20px;top:38px" width="332" height="150" viewBox="0 0 332 150">
      <rect x="40" y="0" width="90" height="10" fill="#3a9b35"/><rect x="132" y="0" width="90" height="10" fill="#8cc63f"/><rect x="224" y="0" width="90" height="10" fill="#999"/>
      <g font-family="Montserrat" font-size="4.5" fill="#fff" text-anchor="middle"><text x="85" y="7">TEXT HERE</text><text x="177" y="7">TEXT HERE</text><text x="269" y="7">TEXT HERE</text></g>
      <g fill="#2c2c2c"><rect x="14" y="16" width="14" height="14"/><rect x="14" y="40" width="14" height="14"/><rect x="14" y="64" width="14" height="14"/><rect x="14" y="88" width="14" height="14"/><rect x="14" y="112" width="14" height="14"/></g>
      <g stroke="#e3e6e1"><line x1="40" y1="35" x2="314" y2="35"/><line x1="40" y1="59" x2="314" y2="59"/><line x1="40" y1="83" x2="314" y2="83"/><line x1="40" y1="107" x2="314" y2="107"/></g>
      <g font-family="Montserrat" font-size="4.5" fill="#666" text-anchor="middle"><text x="85" y="25">Add Content Title</text><text x="177" y="25">Add Content Title</text><text x="269" y="25">Add Content Title</text><text x="85" y="49">Modern Layout</text><text x="177" y="49">Modern Layout</text><text x="269" y="49">Modern Layout</text><text x="85" y="73">Add Content Title</text><text x="177" y="73">Add Content Title</text><text x="269" y="73">Add Content Title</text><text x="85" y="97">Modern Layout</text><text x="177" y="97">Modern Layout</text><text x="269" y="97">Modern Layout</text><text x="85" y="121">Add Content Title</text><text x="177" y="121">Add Content Title</text><text x="269" y="121">Add Content Title</text></g>
    </svg><div class="foot"></div></div>

  <div class="slide"><div class="t">Text with Graph</div><div class="mark">Brookvane Cargo</div>
    <div class="abs" style="left:14px;top:45px;width:120px"><div class="h">Content Here</div><div class="p">You can simply impress your audience and add a unique zing and appeal to your presentation. Easy to change colors, photos and text.</div></div>
    <svg class="abs" style="left:150px;top:40px" width="210" height="150" viewBox="0 0 210 150">
      <g stroke="#eee"><line x1="20" y1="20" x2="205" y2="20"/><line x1="20" y1="50" x2="205" y2="50"/><line x1="20" y1="80" x2="205" y2="80"/><line x1="20" y1="110" x2="205" y2="110"/></g>
      <path d="M25 30 C60 30 70 110 100 105 S150 40 200 60" fill="none" stroke="#3a9b35" stroke-width="1.2"/>
      <path d="M25 60 C60 70 80 90 110 70 S160 80 200 50" fill="none" stroke="#8cc63f" stroke-width="1.2"/>
      <path d="M25 90 C60 85 90 60 120 75 S170 95 200 85" fill="none" stroke="#bbb" stroke-width="1.2"/>
    </svg><div class="foot"></div></div>

  <div class="slide dark"><div class="mark" style="color:var(--lime)">Brookvane Cargo</div>
    <div class="abs" style="left:220px;top:110px"><div style="display:inline-block;border:1px solid #fff;font-size:10px;font-weight:700;padding:1px 4px">01</div><div style="font-size:13px;font-weight:700;color:var(--lime);margin-top:4px">SECTION TITLE</div><div class="p" style="color:#bbb;width:130px">Add a short note here to explain this section.</div></div></div>

  <div class="slide greenbg"><div class="abs" style="right:0;top:0;width:100px;height:40px;background:var(--dark)"><div class="mark" style="color:var(--lime)">Brookvane Cargo</div></div>
    <div class="abs" style="left:220px;top:110px;color:#fff"><div style="font-size:10px;font-weight:700">02</div><div style="font-size:13px;font-weight:700;margin-top:4px">SECTION TITLE</div><div class="p" style="color:#e5f3d8;width:130px">Add a short note here to explain this section.</div></div></div>

  <div class="slide"><div class="t">Our Process</div><div class="mark">Brookvane Cargo</div>
    <svg class="abs" style="left:14px;top:58px" width="344" height="36" viewBox="0 0 344 36">
      <polygon points="0,0 60,0 70,18 60,36 0,36 10,18" fill="#3a9b35"/><polygon points="68,0 128,0 138,18 128,36 68,36 78,18" fill="#8cc63f"/><polygon points="136,0 196,0 206,18 196,36 136,36 146,18" fill="#2c2c2c"/><polygon points="204,0 264,0 274,18 264,36 204,36 214,18" fill="#3a9b35"/><polygon points="272,0 332,0 342,18 332,36 272,36 282,18" fill="#8cc63f"/>
      <g font-family="Montserrat" font-size="5" fill="#fff" text-anchor="middle"><text x="37" y="30">Step 01</text><text x="105" y="30">Step 02</text><text x="173" y="30">Step 03</text><text x="241" y="30">Step 04</text><text x="309" y="30">Step 05</text></g>
    </svg>
    <div class="cols" style="grid-template-columns:repeat(5,1fr);top:108px;gap:6px"><div><div class="h">Content Here</div><div class="p">Add a short note here to explain this step.</div></div><div><div class="h">Content Here</div><div class="p">Add a short note here to explain this step.</div></div><div><div class="h">Content Here</div><div class="p">Add a short note here to explain this step.</div></div><div><div class="h">Content Here</div><div class="p">Add a short note here to explain this step.</div></div><div><div class="h">Content Here</div><div class="p">Add a short note here to explain this step.</div></div></div><div class="foot"></div></div>

  <div class="slide"><div class="t">Our Process</div><div class="mark">Brookvane Cargo</div>
    <div class="abs" style="left:14px;right:14px;top:70px;border-top:1px dashed #ccc"></div>
    <div class="cols" style="grid-template-columns:repeat(6,1fr);top:60px;gap:6px;text-align:center">
      <div><div style="width:20px;height:20px;margin:0 auto 8px;border-radius:50%;border:1px solid var(--green);background:#fff"></div><div class="h">LOREM IPSUM</div><div class="p">Add a short note here.</div></div>
      <div><div style="width:20px;height:20px;margin:0 auto 8px;border-radius:50%;border:1px solid var(--green);background:#fff"></div><div class="h">LOREM IPSUM</div><div class="p">Add a short note here.</div></div>
      <div><div style="width:20px;height:20px;margin:0 auto 8px;border-radius:50%;border:1px solid var(--green);background:#fff"></div><div class="h">LOREM IPSUM</div><div class="p">Add a short note here.</div></div>
      <div><div style="width:20px;height:20px;margin:0 auto 8px;border-radius:50%;border:1px solid var(--green);background:#fff"></div><div class="h">LOREM IPSUM</div><div class="p">Add a short note here.</div></div>
      <div><div style="width:20px;height:20px;margin:0 auto 8px;border-radius:50%;border:1px solid var(--green);background:#fff"></div><div class="h">LOREM IPSUM</div><div class="p">Add a short note here.</div></div>
      <div><div style="width:20px;height:20px;margin:0 auto 8px;border-radius:50%;border:1px solid var(--green);background:#fff"></div><div class="h">LOREM IPSUM</div><div class="p">Add a short note here.</div></div>
    </div><div class="foot"></div></div>

  <div class="slide"><div class="t">Our Team</div><div class="mark">Brookvane Cargo</div>
    <div class="cols" style="grid-template-columns:repeat(4,1fr);top:36px;gap:10px;text-align:center">
      <div><div class="ph people" role="img" aria-label="Portrait of a team member" style="height:70px"></div><div style="background:var(--green);color:#fff;font-size:5px;padding:2px">Member Name</div><div class="p" style="margin-top:4px">Add a short note here.</div></div>
      <div><div class="ph people" role="img" aria-label="Portrait of a team member" style="height:70px"></div><div style="background:var(--lime);color:#fff;font-size:5px;padding:2px">Member Name</div><div class="p" style="margin-top:4px">Add a short note here.</div></div>
      <div><div class="ph people" role="img" aria-label="Portrait of a team member" style="height:70px"></div><div style="background:var(--green);color:#fff;font-size:5px;padding:2px">Member Name</div><div class="p" style="margin-top:4px">Add a short note here.</div></div>
      <div><div class="ph people" role="img" aria-label="Portrait of a team member" style="height:70px"></div><div style="background:var(--lime);color:#fff;font-size:5px;padding:2px">Member Name</div><div class="p" style="margin-top:4px">Add a short note here.</div></div>
    </div><div class="foot"></div></div>

  <div class="slide"><div class="t">Infographic Style</div><div class="mark">Brookvane Cargo</div>
    <div class="abs" style="left:24px;top:50px;width:140px;height:120px;background:#f4f8ef"><div class="abs" style="left:10px;top:6px;width:22px;height:22px;border-radius:50%;background:var(--green);color:#fff;font-size:12px;font-weight:700;text-align:center;line-height:22px">$</div><div class="abs" style="left:20px;top:30px;font-size:40px;font-weight:800;color:var(--green)">08</div><div class="abs" style="left:90px;top:62px;background:var(--green);color:#fff;font-size:4px;padding:1px 4px">COST</div><div class="abs" style="left:50px;top:84px;font-size:9px;font-weight:600;color:var(--green)">Million</div></div>
    <div class="abs" style="left:190px;top:44px;font-size:30px;font-weight:800;color:var(--lime)">04</div><div class="abs" style="left:240px;top:56px;background:var(--lime);color:#fff;font-size:4px;padding:1px 4px">SALES</div><div class="abs" style="left:245px;top:70px;font-size:7px">Million</div><div class="abs p" style="left:290px;top:50px;width:60px">Add a short note here.</div>
    <div class="abs" style="left:190px;top:120px;font-size:30px;font-weight:800;color:var(--dark)">15</div><div class="abs" style="left:240px;top:134px;background:var(--dark);color:#fff;font-size:4px;padding:1px 4px">PERCENTAGE</div><div class="abs p" style="left:290px;top:126px;width:60px">Add a short note here.</div>
    <div class="foot"></div></div>

  <div class="slide"><div class="t">Pyramid Infographic</div><div class="mark">Brookvane Cargo</div>
    <svg class="abs" style="left:130px;top:40px" width="110" height="150" viewBox="0 0 110 150">
      <polygon points="55,0 72,37 38,37" fill="#8cc63f"/><polygon points="38,39 72,39 88,74 22,74" fill="#3a9b35"/><polygon points="22,76 88,76 104,111 6,111" fill="#2c2c2c"/><polygon points="6,113 104,113 110,130 0,130" fill="#aaa"/>
      <g font-family="Montserrat" font-size="5" fill="#fff" text-anchor="middle"><text x="55" y="60">STEP 02</text><text x="55" y="97">STEP 03</text><text x="55" y="124">STEP 04</text></g>
    </svg>
    <div class="abs" style="left:14px;top:50px;width:100px"><div class="h">STEP 01</div><div class="p">Add a short note here to explain this step.</div></div><div class="abs" style="left:14px;top:120px;width:100px"><div class="h">STEP 02</div><div class="p">Add a short note here to explain this step.</div></div>
    <div class="abs" style="left:262px;top:50px;width:100px"><div class="h">STEP 03</div><div class="p">Add a short note here to explain this step.</div></div><div class="abs" style="left:262px;top:120px;width:100px"><div class="h">STEP 04</div><div class="p">Add a short note here to explain this step.</div></div>
    <div class="foot"></div></div>

  <div class="slide"><div class="t">Funnel Infographic</div><div class="mark">Brookvane Cargo</div>
    <svg class="abs" style="left:130px;top:42px" width="110" height="150" viewBox="0 0 110 150">
      <ellipse cx="55" cy="12" rx="52" ry="10" fill="#8cc63f"/><path d="M3 12 L20 60 L90 60 L107 12 A52 10 0 0 1 3 12" fill="#3a9b35"/><path d="M22 64 L33 98 L77 98 L88 64Z" fill="#2c2c2c"/><path d="M35 102 L44 132 L66 132 L75 102Z" fill="#3a9b35"/>
      <g font-family="Montserrat" font-size="5" fill="#fff" text-anchor="middle"><text x="55" y="40">STEP 01</text><text x="55" y="84">STEP 02</text><text x="55" y="120">STEP 03</text></g>
    </svg>
    <div class="abs" style="left:14px;top:50px;width:100px"><div class="h">STEP 01</div><div class="p">Add a short note here to explain this step.</div></div><div class="abs" style="left:14px;top:120px;width:100px"><div class="h">STEP 02</div><div class="p">Add a short note here to explain this step.</div></div>
    <div class="abs" style="left:262px;top:50px;width:100px"><div class="h">STEP 03</div><div class="p">Add a short note here to explain this step.</div></div><div class="abs" style="left:262px;top:120px;width:100px"><div class="h">STEP 04</div><div class="p">Add a short note here to explain this step.</div></div>
    <div class="foot"></div></div>

  <div class="slide"><div class="t">Frameworks</div><div class="mark">Brookvane Cargo</div>
    <svg class="abs" style="left:141px;top:40px" width="90" height="150" viewBox="0 0 90 150">
      <circle cx="45" cy="40" r="18" fill="#8cc63f"/><circle cx="73" cy="60" r="18" fill="#999"/><circle cx="73" cy="95" r="18" fill="#2c2c2c"/><circle cx="45" cy="115" r="18" fill="#555"/><circle cx="17" cy="95" r="18" fill="#3a9b35"/><circle cx="17" cy="60" r="18" fill="#1f7a34"/><circle cx="45" cy="77" r="10" fill="#fff"/>
    </svg>
    <div class="abs" style="left:14px;top:50px;width:110px"><div class="h">Content 01</div><div class="p">Add a short note here to explain this point.</div></div><div class="abs" style="left:14px;top:130px;width:110px"><div class="h">Content 03</div><div class="p">Add a short note here to explain this point.</div></div>
    <div class="abs" style="left:250px;top:50px;width:110px"><div class="h">Content 02</div><div class="p">Add a short note here to explain this point.</div></div><div class="abs" style="left:250px;top:130px;width:110px"><div class="h">Content 04</div><div class="p">Add a short note here to explain this point.</div></div>
    <div class="foot"></div></div>

  <div class="slide"><div class="t">Our Services Offers</div><div class="mark">Brookvane Cargo</div>
    <div class="cols" style="grid-template-columns:repeat(4,1fr);top:40px;gap:8px;text-align:center">
      <div><div class="ph road" role="img" aria-label="Photo of a parcel handover" style="height:70px"></div><div style="background:var(--green);color:#fff;font-size:5px;padding:2px">Offer 01</div><div class="p" style="margin-top:4px">Add a short note here.</div></div>
      <div><div class="ph people" role="img" aria-label="Photo of a delivery courier" style="height:70px"></div><div style="background:var(--lime);color:#fff;font-size:5px;padding:2px">Offer 02</div><div class="p" style="margin-top:4px">Add a short note here.</div></div>
      <div><div class="ph road" role="img" aria-label="Photo of a courier with parcels" style="height:70px"></div><div style="background:var(--green);color:#fff;font-size:5px;padding:2px">Offer 03</div><div class="p" style="margin-top:4px">Add a short note here.</div></div>
      <div><div class="ph people" role="img" aria-label="Photo of a customer service agent" style="height:70px"></div><div style="background:var(--lime);color:#fff;font-size:5px;padding:2px">Offer 04</div><div class="p" style="margin-top:4px">Add a short note here.</div></div>
    </div><div class="foot"></div></div>

  <div class="slide"><div class="t">KPIs/scorecard</div><div class="mark">Brookvane Cargo</div>
    <div class="cols" style="grid-template-columns:repeat(4,1fr);top:36px;gap:10px">
      <div><div style="font-size:16px;font-weight:700;color:var(--green)">01</div><div style="background:#f4f4f4;height:90px;padding:6px"><div class="h" style="color:var(--ink)">Content Here</div><div class="p">Add a short note here to explain this metric.</div></div></div>
      <div><div style="font-size:16px;font-weight:700;color:var(--lime)">02</div><div style="background:#f4f4f4;height:90px;padding:6px"><div class="h" style="color:var(--ink)">Content Here</div><div class="p">Add a short note here to explain this metric.</div></div></div>
      <div><div style="font-size:16px;font-weight:700;color:var(--dark)">03</div><div style="background:#f4f4f4;height:90px;padding:6px"><div class="h" style="color:var(--ink)">Content Here</div><div class="p">Add a short note here to explain this metric.</div></div></div>
      <div><div style="font-size:16px;font-weight:700;color:#999">04</div><div style="background:#f4f4f4;height:90px;padding:6px"><div class="h" style="color:var(--ink)">Content Here</div><div class="p">Add a short note here to explain this metric.</div></div></div>
    </div><div class="foot"></div></div>

  <div class="slide"><div class="mark" style="left:14px;right:auto">Brookvane Cargo</div>
    <div class="abs" style="left:14px;top:60px;width:140px"><div style="font-size:11px;font-weight:700">Mission<br>Statement</div><div class="p" style="margin-top:6px">You can simply impress your audience and add a unique zing and appeal to your presentation. Easy to change colors, photos and text.</div></div>
    <div class="abs ph soft" role="img" aria-label="Hands holding a young tree in soil" style="right:0;top:0;width:190px;height:209px;border-radius:60px 0 0 0"></div><div class="foot"></div></div>

  <div class="slide"><div class="t">Our Structure</div><div class="mark">Brookvane Cargo</div>
    <svg class="abs" style="left:30px;top:40px" width="150" height="150" viewBox="0 0 150 150">
      <g fill="none" stroke-width="22" transform="rotate(-90 75 75)"><circle cx="75" cy="75" r="55" stroke="#999" stroke-dasharray="172.8 345.6"/><circle cx="75" cy="75" r="55" stroke="#3a9b35" stroke-dasharray="103.7 345.6" stroke-dashoffset="-172.8"/><circle cx="75" cy="75" r="55" stroke="#8cc63f" stroke-dasharray="34.6 345.6" stroke-dashoffset="-276.5"/><circle cx="75" cy="75" r="55" stroke="#2c2c2c" stroke-dasharray="34.5 345.6" stroke-dashoffset="-311.1"/></g>
      <g font-family="Montserrat" font-size="7" font-weight="700" fill="#fff" text-anchor="middle"><text x="128" y="78">50%</text><text x="38" y="118">30%</text><text x="24" y="62">10%</text><text x="50" y="28">10%</text></g>
    </svg>
    <div class="abs" style="left:220px;top:50px;width:140px;display:grid;row-gap:8px"><div class="p">• Add a short note here to explain this part.</div><div class="p">• Add a short note here to explain this part.</div><div class="p">• Add a short note here to explain this part.</div><div class="p">• Add a short note here to explain this part.</div></div>
    <div class="foot"></div></div>

  <div class="slide"><div class="t">Activities/ToDo page</div><div class="mark">Brookvane Cargo</div>
    <div class="cols" style="grid-template-columns:1fr 1fr;top:40px;row-gap:10px">
      <div class="row"><span class="num" style="border-radius:3px">✓</span><div><div class="h">Content Here</div><div class="p">Add a short note here to explain this task.</div></div></div>
      <div class="row"><span class="num" style="border-radius:3px">✓</span><div><div class="h">Content Here</div><div class="p">Add a short note here to explain this task.</div></div></div>
      <div class="row"><span class="num" style="border-radius:3px;background:var(--lime)">✓</span><div><div class="h">Content Here</div><div class="p">Add a short note here to explain this task.</div></div></div>
      <div class="row"><span class="num" style="border-radius:3px;background:var(--lime)">✓</span><div><div class="h">Content Here</div><div class="p">Add a short note here to explain this task.</div></div></div>
      <div class="row"><span class="num dk" style="border-radius:3px">✓</span><div><div class="h">Content Here</div><div class="p">Add a short note here to explain this task.</div></div></div>
      <div class="row"><span class="num dk" style="border-radius:3px">✓</span><div><div class="h">Content Here</div><div class="p">Add a short note here to explain this task.</div></div></div>
    </div><div class="foot"></div></div>

  <div class="slide"><div class="abs ph people" role="img" aria-label="Smiling professional woman at work" style="left:0;top:0;width:180px;height:209px;border-radius:0 0 60px 0"></div><div class="mark">Brookvane Cargo</div>
    <div class="abs" style="left:200px;top:70px;width:150px"><div style="font-size:11px;font-weight:700">Vision<br>Statement</div><div class="p" style="margin-top:6px">You can simply impress your audience and add a unique zing and appeal to your presentation. Easy to change colors, photos and text.</div></div><div class="foot"></div></div>

  <div class="slide"><div class="abs ph" role="img" aria-label="Many hands holding a small plant together" style="left:0;top:0;width:190px;height:209px;filter:brightness(.75)"></div>
    <div class="abs" style="left:12px;top:10px;background:var(--dark);color:#fff;font-size:10px;font-weight:700;padding:3px 8px">Evaluation Results</div>
    <div class="abs p" style="left:14px;top:150px;width:160px;color:#fff">Add a short note here to explain the overall result of this evaluation.</div>
    <div class="mark">Brookvane Cargo</div>
    <div class="abs" style="left:205px;top:50px;width:155px;display:grid;row-gap:12px">
      <div class="row"><span class="num" style="border-radius:3px">!</span><div><div class="h">Challenge</div><div class="p">Add a short note here to explain this.</div></div></div>
      <div class="row"><span class="num" style="border-radius:3px;background:var(--lime)">✓</span><div><div class="h">Solution</div><div class="p">Add a short note here to explain this.</div></div></div>
      <div class="row"><span class="num dk" style="border-radius:3px">★</span><div><div class="h">Result</div><div class="p">Add a short note here to explain this.</div></div></div>
    </div><div class="foot"></div></div>

  <div class="slide"><div class="t">Career Path</div><div class="mark">Brookvane Cargo</div>
    <svg class="abs" style="left:116px;top:40px" width="140" height="160" viewBox="0 0 140 160">
      <circle cx="70" cy="18" r="12" fill="#8cc63f"/>
      <rect x="50" y="40" width="40" height="16" fill="#3a9b35"/><rect x="38" y="58" width="64" height="16" fill="#2c2c2c"/><rect x="26" y="76" width="88" height="16" fill="#3a9b35"/><rect x="14" y="94" width="112" height="16" fill="#2c2c2c"/><rect x="2" y="112" width="136" height="18" fill="#3a9b35"/>
      <g font-family="Montserrat" font-size="5" fill="#fff" text-anchor="middle"><text x="70" y="51">LEVEL 5</text><text x="70" y="69">STRATEGY</text><text x="70" y="87">MARKETING</text><text x="70" y="105">TEAMWORK</text><text x="70" y="124">DEVELOPMENT</text></g>
    </svg>
    <div class="abs" style="left:14px;top:50px;width:90px"><div class="h">STRATEGY</div><div class="p">Add a short note here to explain this stage.</div></div><div class="abs" style="left:14px;top:130px;width:90px"><div class="h">TEAMWORK</div><div class="p">Add a short note here to explain this stage.</div></div>
    <div class="abs" style="left:270px;top:50px;width:90px"><div class="h">MARKETING</div><div class="p">Add a short note here to explain this stage.</div></div><div class="abs" style="left:270px;top:130px;width:90px"><div class="h">DEVELOPMENT</div><div class="p">Add a short note here to explain this stage.</div></div>
    <div class="foot"></div></div>

  <div class="slide"><div class="t">Free Vector Icons</div><div class="mark">Brookvane Cargo</div>
    <svg class="abs" style="left:14px;top:36px" width="344" height="160" viewBox="0 0 344 160">
      <defs>
        <g id="i-a"><circle cx="6" cy="6" r="5" fill="none" stroke="#555" stroke-width="1"/><path d="M3.5 6 l2 2 l3-4" fill="none" stroke="#555" stroke-width="1"/></g>
        <g id="i-b"><rect x="1" y="1" width="10" height="10" rx="1.5" fill="none" stroke="#555" stroke-width="1"/><line x1="3" y1="5" x2="9" y2="5" stroke="#555"/></g>
        <g id="i-c"><path d="M6 1 a4 4 0 0 1 4 4 c0 3-4 6-4 6 s-4-3-4-6 a4 4 0 0 1 4-4z" fill="none" stroke="#555" stroke-width="1"/></g>
        <g id="i-d"><path d="M2 6 h8 M7 3 l3 3 l-3 3" fill="none" stroke="#555" stroke-width="1"/></g>
        <g id="i-row"><use href="#i-a" x="0"/><use href="#i-b" x="22"/><use href="#i-c" x="44"/><use href="#i-d" x="66"/><use href="#i-b" x="88"/><use href="#i-a" x="110"/><use href="#i-d" x="132"/><use href="#i-c" x="154"/><use href="#i-a" x="176"/><use href="#i-b" x="198"/><use href="#i-c" x="220"/><use href="#i-d" x="242"/><use href="#i-a" x="264"/><use href="#i-b" x="286"/><use href="#i-c" x="308"/><use href="#i-d" x="330"/></g>
      </defs>
      <use href="#i-row" y="0"/><use href="#i-row" y="20"/><use href="#i-row" y="40"/><use href="#i-row" y="60"/><use href="#i-row" y="80"/><use href="#i-row" y="100"/><use href="#i-row" y="120"/><use href="#i-row" y="140"/>
    </svg><div class="foot"></div></div>

  <div class="slide"><div class="abs" style="left:26px;top:22px;font-size:12px;font-weight:800">THANK YOU</div>
    <div class="abs" style="left:26px;top:48px;background:var(--green);color:#fff;font-size:5px;padding:2px 8px">Contact Us</div>
    <div class="abs p" style="left:26px;top:62px;width:110px">Add a short note here to close your presentation.</div>
    <div class="abs p" style="left:26px;top:100px;line-height:2.4">☎ +49 000 000 000<br>✉ hello@brookvane-cargo.de<br>⌂ www.brookvane-cargo.de</div>
    <div class="abs" style="right:20px;top:60px;width:180px;text-align:center"><div style="width:34px;height:34px;border-radius:50%;background:var(--green);margin:0 auto 8px"></div><div style="font-size:14px;font-weight:800;color:var(--green);white-space:nowrap">BROOKVANE CARGO</div><div style="font-size:5px;color:var(--mute);letter-spacing:2px;margin-top:4px">ZERO-EMISSION CITY DELIVERY</div></div>
    <div class="foot"></div></div>

</main>
</body>
</html>
```